ROLLFAST FITNESSRoll Out, A UNIQUE CONCIERGE MOBILE SERVICE LAUNCHING in SOUTH FLORIDA

I AM LOOKING TO ATTRACT LEADS FOR CONVERSION WHILE BRINGING OUR SERVICE TO LIFE IN THERE HANDS. WE SERVICE A VERY HIGHLY AFFLUENT CROWD. I would like those on a 5 x 7 two sided card

Target Market(s)

AFFLUENT

Industry/Entity Type

HEALTH AND FITNESS

Font styles to use
Other font styles liked:
• POPINS MED

Colors
0054AA
0677BA
7BADD7
CADEEF
E8F1F8
FFF300
FFF600
FEFA6F
FFFEC7
FFFEE8

Requirements
Must have
• space for postage I INCLUDED CONTENT
Nice to have
• CLASSY FUN LOOK
Should not have
• DULLNESs

```html
<!DOCTYPE html>
<html lang="en">
<head>
<meta charset="utf-8">
<title>Skybend Fitness – Postcard</title>
<link rel="stylesheet" href="https://fonts.googleapis.com/css2?family=Poppins:wght@400;500;600&display=swap">
<style>
  :root {
    --page-bg: #dcdcdc;
    --shadow: #b3b3b3;
    --sky-blue: #4fbdd1;
    --sun-yellow: #ffdd00;
    --headline-yellow: #ffe500;
    --ink: #4a4a52;
    --paper: #ffffff;
    --stamp-grey: #b3b3b3;
    --rule: #555559;
    --photo-light: #d9d6cf;
    --photo-mid: #8d8a84;
    --photo-dark: #3e3e42;
  }
  html, body {
    margin: 0;
    padding: 0;
    width: 1200px;
    height: 1200px;
    overflow: hidden;
    background: var(--page-bg);
  }
  .sheet {
    position: relative;
    width: 1200px;
    height: 1200px;
    font-family: "Poppins", sans-serif;
  }
  .card {
    position: absolute;
    left: 187px;
    width: 788px;
    height: 562px;
  }
  .card--front { top: 29px; }
  .card--back { top: 614px; }
  .card__shadow {
    position: absolute;
    left: 9px;
    top: 9px;
    width: 788px;
    height: 562px;
    background: var(--shadow);
  }
  .card__face {
    position: absolute;
    inset: 0;
    width: 788px;
    height: 562px;
    display: block;
  }
  .brand-name { font-weight: 600; fill: var(--ink); letter-spacing: 1px; }
  .tagline { font-weight: 500; fill: var(--ink); }
  .contact { font-weight: 400; fill: var(--ink); }
  .cta-label { font-weight: 400; fill: var(--ink); letter-spacing: 0.5px; }
  .promise { font-weight: 500; fill: var(--headline-yellow); }
  .benefits { font-weight: 400; fill: var(--ink); }
  .invite { font-weight: 500; fill: var(--ink); }
  .link { font-weight: 500; fill: var(--ink); }
</style>
</head>
<body>
<main class="sheet">

  <section class="card card--front" aria-label="Postcard front">
    <div class="card__shadow"></div>
    <svg class="card__face" viewBox="0 0 1268 905" xmlns="http://www.w3.org/2000/svg">
      <defs>
        <linearGradient id="truckPhotoTone" x1="0" y1="0" x2="0" y2="1">
          <stop offset="0" stop-color="var(--photo-light)"/>
          <stop offset="0.35" stop-color="var(--photo-mid)"/>
          <stop offset="0.65" stop-color="var(--photo-dark)"/>
          <stop offset="1" stop-color="var(--photo-mid)"/>
        </linearGradient>
      </defs>
      <rect class="front-base" width="1268" height="905" fill="var(--sky-blue)"/>
      <polygon class="truck-photo" points="554,0 1268,0 1268,905 664,905" fill="url(#truckPhotoTone)" role="img" aria-label="Photo of the branded mobile fitness truck with training gear set up beside it under a cloudy sky"/>
      <polygon class="headline-band" points="0,217 580,217 605,689 0,689" fill="var(--sun-yellow)"/>

      <text class="brand-name" x="68" y="112" font-size="38">SKYBEND FITNESS</text>

      <text class="tagline" x="42" y="317" font-size="45">"Get Fit on Your</text>
      <text class="tagline" x="42" y="414" font-size="88">Schedule,</text>
      <text class="tagline" x="42" y="510" font-size="88">Anywhere,</text>
      <text class="tagline" x="42" y="605" font-size="88">Anytime.”</text>

      <g class="phone-icon" transform="translate(34,773)" fill="var(--ink)">
        <path d="M6 2 L16 0 L24 16 L17 22 Q22 34 33 40 L39 33 L52 41 L50 50 Q46 54 38 52 Q10 42 2 14 Q0 6 6 2 Z"/>
      </g>
      <text class="contact" x="115" y="812" font-size="38">+1 (555) 014-2290</text>

      <polygon class="cta-ribbon" points="500,761 1167,761 1201,843 527,843" fill="var(--sun-yellow)"/>
      <text class="cta-label" x="597" y="812" font-size="31">CALL FOR FREE CONSULTATION</text>
    </svg>
  </section>

  <section class="card card--back" aria-label="Postcard back">
    <div class="card__shadow"></div>
    <svg class="card__face" viewBox="0 0 1268 905" xmlns="http://www.w3.org/2000/svg">
      <rect class="back-base" width="1268" height="905" fill="var(--paper)"/>
      <path class="promise-panel" d="M0,105 H530 Q575,105 592,145 L645,330 Q665,405 598,435 H0 Z" fill="var(--sky-blue)"/>
      <path class="accent-column" d="M1150,63 H1268 V824 H1195 V520 H1120 L1090,150 Q1086,63 1150,63 Z" fill="var(--sun-yellow)"/>

      <text class="promise" x="35" y="190" font-size="44">Transform Your Body,</text>
      <text class="promise" x="35" y="246" font-size="44">Mind and Spirit with</text>
      <text class="promise" x="35" y="302" font-size="44">Skybend Fitness.</text>
      <text class="benefits" x="35" y="351" font-size="25">Overall Health, Flexibility, Agility,</text>
      <text class="benefits" x="35" y="383" font-size="25">Strength, We’ve Got you covered</text>

      <text class="invite" x="850" y="172" font-size="23" text-anchor="middle">Get Started with Skybend Fitness</text>
      <text class="invite" x="850" y="202" font-size="23" text-anchor="middle">Today FOR FREE CONSULTAION AND</text>
      <text class="invite" x="850" y="232" font-size="23" text-anchor="middle">ASSESMENT GO TO</text>

      <g class="globe-icon" fill="none" stroke="var(--ink)" stroke-width="2.4">
        <circle cx="675" cy="287" r="13"/>
        <ellipse cx="675" cy="287" rx="5.5" ry="13"/>
        <line x1="662" y1="287" x2="688" y2="287"/>
        <line x1="664" y1="280" x2="686" y2="280"/>
        <line x1="664" y1="294" x2="686" y2="294"/>
      </g>
      <text class="link" x="713" y="294" font-size="22">www.skybendfitness.com</text>

      <g class="mail-icon" fill="none" stroke="var(--ink)" stroke-width="2.2">
        <rect x="687" y="324" width="26" height="18"/>
        <polyline points="687,324 700,335 713,324"/>
        <line x1="687" y1="342" x2="697" y2="333"/>
        <line x1="713" y1="342" x2="703" y2="333"/>
      </g>
      <text class="link" x="731" y="341" font-size="20">info@skybendfit.com</text>

      <g class="address-lines" stroke="var(--rule)" stroke-width="2">
        <line x1="73" y1="555" x2="866" y2="555"/>
        <line x1="73" y1="654" x2="866" y2="654"/>
        <line x1="73" y1="735" x2="866" y2="735"/>
        <line x1="73" y1="828" x2="866" y2="828"/>
      </g>

      <rect class="stamp-frame" x="954" y="521" width="243" height="298" fill="var(--paper)"/>
      <rect class="stamp-box" x="961" y="529" width="229" height="284" fill="var(--stamp-grey)"/>
    </svg>
  </section>

</main>
</body>
</html>
```